Animal Facility Brochure for Pet Boarding, Boutique, Doggie Daycare, Grooming

This brochure is for a Doggie Daycare, Pet Grooming, Dog Boarding & Pet Boutique for the Hollowmere Pet Lodge & Spa.

Hi there! I am in need of a brochure done for my new up and coming business.
The business will involve Dog/Cat Grooming, Dog Boarding, Doggie Daycare, & a small pet boutique. I am looking for something that stands out and is modern and chic and follows the look of the pictures i have posted (Pim and Tessel) . My color scheme of my business is gray & white. Also i need the brochure to be easily able to understand what we are trying to get across and is easy to read. I am very proud of my logo that was created using craft hive and would love that incorporated. also i have attached the information that will need to be in the brochure for the client. I am looking for someone who can devote some time working with me on this because this is my first time. I am sure there will need to be some changes so i need someone who is patient. The picture of the projected look of my sign is gearing more towards something clean and modern.

Industry/Entity Type

Pet Care

Colors
f5f5f5
f8f8f8
dbdbdb
959595
aaaaaa
85abd2
cedeed
eaf1f7

Requirements
Nice to have
• File nine for Grooming, Boarding, Daycare, Pet Boutique

```html
<!DOCTYPE html>
<html lang="en">
<head>
<meta charset="utf-8">
<title>Hollowmere Pet Lodge &amp; Spa — Brochure</title>
<link href="https://fonts.googleapis.com/css2?family=Jost:wght@400;500;600&family=Libre+Baskerville:wght@700&display=swap" rel="stylesheet">
<style>
  :root {
    --stage: #2b2b2b;
    --paper: #f6f6f6;
    --paper-edge: #e6e6e6;
    --ink: #1f1f1f;
    --brown: #4a2c20;
    --rule: #b9b9b9;
    --photo-cream: #e9dcc3;
    --photo-light: #f1ede6;
    --photo-orange: #e3b27a;
    --photo-gray: #9a9a9e;
  }
  * { box-sizing: border-box; margin: 0; padding: 0; }
  html, body { width: 1200px; height: 800px; overflow: hidden; }
  body {
    background: var(--stage);
    font-family: "Jost", sans-serif;
    color: var(--ink);
  }
  .brochure {
    position: absolute;
    left: 42px; top: 20px;
    width: 1116px; height: 760px;
    display: flex;
    box-shadow: 0 10px 30px rgba(0,0,0,.5);
  }
  .panel {
    width: 372px; height: 100%;
    background: linear-gradient(180deg, #fbfbfb 0%, var(--paper) 60%, var(--paper-edge) 100%);
    position: relative;
    display: flex; flex-direction: column; align-items: center;
    text-align: center;
  }
  .panel + .panel { border-left: 1px solid #dcdcdc; }

  /* Mission panel */
  .mission { padding-top: 44px; }
  .mission-title {
    font-family: "Libre Baskerville", serif;
    font-weight: 700; font-size: 22px; color: var(--brown);
    margin-bottom: 12px;
  }
  .mission-text {
    font-size: 14.5px; line-height: 1.42;
    padding: 0 34px;
  }
  .mission-photo {
    position: absolute; left: 0; bottom: 0;
    width: 100%; height: 330px;
    background: linear-gradient(160deg, var(--photo-light) 0%, #f7f3ec 40%, var(--photo-cream) 75%, #d9c7a6 100%);
  }

  /* Hours panel */
  .hours { padding-top: 40px; }
  .hours-photo {
    width: 270px; height: 180px;
    background: radial-gradient(ellipse at 35% 60%, var(--photo-orange) 0%, #efd3ad 45%, transparent 72%),
                radial-gradient(ellipse at 72% 50%, #e8b46e 0%, #f0d5ad 45%, transparent 72%);
    margin-bottom: 22px;
  }
  .hours-title {
    font-family: "Libre Baskerville", serif;
    font-weight: 700; font-size: 19px; color: var(--brown);
    letter-spacing: .5px;
    margin-bottom: 16px;
  }
  .hours-list { list-style: none; font-size: 20px; font-weight: 500; line-height: 1.6; }
  .contact { margin-top: 18px; width: 250px; font-size: 14px; }
  .contact-item { padding: 8px 0 10px; display: flex; flex-direction: column; align-items: center; gap: 4px; }
  .contact-item + .contact-item { border-top: 1px solid var(--rule); }
  .contact-item svg { width: 14px; height: 14px; }
  .contact-web { font-weight: 600; }

  /* Cover panel */
  .cover { padding-top: 46px; }
  .brand { display: flex; align-items: center; gap: 12px; margin-bottom: 24px; }
  .brand-dot { width: 18px; height: 18px; border-radius: 50%; background: var(--brown); }
  .brand-name {
    font-size: 22px; font-weight: 500; color: var(--brown);
    letter-spacing: 2px; text-transform: uppercase; line-height: 1.25;
    text-align: left;
  }
  .cover-photo {
    width: 300px; height: 220px;
    background: radial-gradient(ellipse at 32% 62%, var(--photo-gray) 0%, #c4c4c6 42%, transparent 70%),
                radial-gradient(ellipse at 70% 50%, var(--photo-cream) 0%, #f0e6d4 45%, transparent 72%);
    margin-bottom: 36px;
  }
  .tagline {
    font-family: "Libre Baskerville", serif;
    font-weight: 700; font-size: 18px; line-height: 1.35; color: var(--brown);
    padding: 0 34px;
  }
  .cover-web {
    margin-top: 22px; width: 250px;
    border-top: 1px solid var(--rule); padding-top: 12px;
    font-size: 14px; font-weight: 600;
  }
</style>
</head>
<body>
  <main class="brochure">
    <section class="panel mission">
      <h2 class="mission-title">Our Mission:</h2>
      <p class="mission-text">is to care for your pet in the best way possible when you are away. We provide a unique social experience for dogs and create a new standard for dog care. Our Kitty condo provides a safe and quiet atmosphere for your kitty. We have set out to create a facility that exemplifies what we ourselves would want for our own best friends. Your pet will have a fun, safe place to play during the day and a secure night time environment when lodging with us. Our staff will go to any lengths to make our guest's stay a true delight. Our professional spa and grooming salon offers a wide range of services for your dog and cat. Our experienced groomers are friendly and knowledgeable and have the expertise to help your pet look and feel its best while exceeding your expectations.</p>
      <div class="mission-photo" role="img" aria-label="Photo of a golden retriever lying on a table in a bright room"></div>
    </section>

    <section class="panel hours">
      <div class="hours-photo" role="img" aria-label="Photo of an orange kitten sitting beside a Pomeranian dog"></div>
      <h2 class="hours-title">HOURS OF OPERATION</h2>
      <ul class="hours-list">
        <li>Monday 7:30am- 6:30pm</li>
        <li>Tuesday 7:30am- 6:30pm</li>
        <li>Wednesday 7:30am- 6:30pm</li>
        <li>Thursday 7:30am- 6:30pm</li>
        <li>Friday 7:30am- 6:30pm</li>
        <li>Saturday 8:30am- 6:30pm</li>
        <li>Sunday 10:30am- 6:30pm</li>
      </ul>
      <div class="contact">
        <div class="contact-item">
          <svg viewBox="0 0 14 14" aria-hidden="true"><path d="M7 1a4 4 0 0 0-4 4c0 3 4 8 4 8s4-5 4-8a4 4 0 0 0-4-4z" fill="none" stroke="#4a2c20" stroke-width="1.3"/><circle cx="7" cy="5" r="1.4" fill="#4a2c20"/></svg>
          <span>218 Linden Hollow Road<br>Hollowmere, OH 43012</span>
        </div>
        <div class="contact-item">
          <svg viewBox="0 0 14 14" aria-hidden="true"><rect x="1.5" y="3" width="11" height="8" fill="none" stroke="#4a2c20" stroke-width="1.2"/><path d="M1.5 3l5.5 4.5L12.5 3" fill="none" stroke="#4a2c20" stroke-width="1.2"/></svg>
          <span>info@hollowmerepetlodge.com</span>
        </div>
        <div class="contact-item contact-web">www.hollowmerepetlodge.com</div>
      </div>
    </section>

    <section class="panel cover">
      <div class="brand">
        <span class="brand-dot"></span>
        <span class="brand-name">Hollowmere Pet<br>Lodge &amp; Spa</span>
      </div>
      <div class="cover-photo" role="img" aria-label="Photo of a gray cat and a cream puppy peeking over an edge"></div>
      <p class="tagline">When it comes to your pet, we will stop at nothing to keep them healthy, happy and well-loved</p>
      <div class="cover-web">www.hollowmerepetlodge.com</div>
    </section>
  </main>
</body>
</html>
```